Background graphic for Vortapex profile

I need a graphic for the background image that appears on Vortapex behind my photo.
I am looking for an image that complements my About Me statement, "Directing patient-first marketing from strategy to execution to help healthcare companies reach the right people at just the right time." I am thinking something with a clock and people and connections. A single example is below and I am open to creative ideas.
1128 (w) x 191 (h) pixels, PNG or JPEG files and have a maximum size of 3MB

```html
<!DOCTYPE html>
<html lang="en">
<head>
<meta charset="utf-8">
<title>Vortapex profile background</title>
<link rel="stylesheet" href="https://fonts.googleapis.com/css2?family=Roboto:wght@400&display=swap">
<style>
  :root {
    --teal-light: #4f9ea6;
    --teal-mid: #2e7a86;
    --teal-deep: #1d5361;
    --night: #243a52;
    --badge: #55d3f7;
    --stem: #6fdcf8;
    --icon: #ffffff;
    --trace: rgba(130, 225, 250, 0.55);
  }
  * { margin: 0; padding: 0; box-sizing: border-box; }
  html, body {
    width: 1200px;
    height: 203px;
    overflow: hidden;
    background: var(--teal-deep);
    font-family: "Roboto", sans-serif;
  }
  .banner {
    position: relative;
    width: 1200px;
    height: 203px;
    overflow: hidden;
  }
  .banner__scene,
  .banner__network {
    position: absolute;
    inset: 0;
    width: 1200px;
    height: 203px;
    display: block;
  }
  .stem { stroke: var(--stem); stroke-width: 2; fill: none; }
  .anchor { stroke: var(--stem); stroke-width: 1.5; fill: none; }
  .badge { fill: var(--badge); }
  .glyph { fill: var(--icon); }
  .glyph-line { stroke: var(--icon); fill: none; stroke-linecap: round; }
  .trace { stroke: var(--trace); stroke-width: 1.5; fill: none; }
</style>
</head>
<body>
<main class="banner">
  <svg class="banner__scene" viewBox="0 0 1200 203" role="img"
       aria-label="Night city skyline with silhouettes of people and glowing data dots">
    <defs>
      <linearGradient id="sceneTone" x1="0" y1="0" x2="0" y2="1">
        <stop offset="0" stop-color="var(--teal-light)"/>
        <stop offset="0.55" stop-color="var(--teal-mid)"/>
        <stop offset="1" stop-color="var(--teal-deep)"/>
      </linearGradient>
      <linearGradient id="sceneShade" x1="0" y1="0" x2="1" y2="0">
        <stop offset="0" stop-color="var(--night)" stop-opacity="0.25"/>
        <stop offset="0.5" stop-color="var(--night)" stop-opacity="0"/>
        <stop offset="1" stop-color="var(--night)" stop-opacity="0.2"/>
      </linearGradient>
    </defs>
    <rect width="1200" height="203" fill="url(#sceneTone)"/>
    <rect width="1200" height="203" fill="url(#sceneShade)"/>
  </svg>

  <svg class="banner__network" viewBox="0 0 1200 203" aria-hidden="true">
    <polyline class="trace" points="851,0 876,41 1200,41"/>
    <polyline class="trace" points="1010,0 1025,22 1200,22"/>

    <g class="connection connection--wifi">
      <line class="stem" x1="144" y1="100" x2="144" y2="154"/>
      <circle class="anchor" cx="144" cy="160" r="8"/>
      <circle class="badge" cx="144" cy="71" r="29"/>
      <path class="glyph-line" stroke-width="4" d="M129 67 a21 21 0 0 1 30 0"/>
      <path class="glyph-line" stroke-width="4" d="M134 73 a14 14 0 0 1 20 0"/>
      <circle class="glyph" cx="144" cy="81" r="3.5"/>
    </g>

    <g class="connection connection--location">
      <line class="stem" x1="361" y1="168" x2="361" y2="203"/>
      <circle class="badge" cx="361" cy="132" r="36"/>
      <path class="glyph" d="M361 152 C352 140 347 133 347 125 a14 14 0 0 1 28 0 c0 8 -5 15 -14 27z"/>
      <circle class="badge" cx="361" cy="125" r="5"/>
    </g>

    <g class="connection connection--health">
      <line class="stem" x1="612" y1="114" x2="612" y2="165"/>
      <circle class="anchor" cx="612" cy="172" r="9"/>
      <circle class="badge" cx="612" cy="73" r="41"/>
      <path class="glyph" d="M612 99 C594 86 587 77 587 67 a12 12 0 0 1 25 -5 a12 12 0 0 1 25 5 c0 10 -7 19 -25 32z"/>
      <rect class="badge" x="609" y="61" width="6" height="20"/>
      <rect class="badge" x="602" y="68" width="20" height="6"/>
    </g>

    <g class="connection connection--mobile">
      <line class="stem" x1="818" y1="129" x2="818" y2="184"/>
      <circle class="anchor" cx="818" cy="192" r="9"/>
      <circle class="badge" cx="818" cy="100" r="29"/>
      <rect class="glyph" x="808" y="82" width="20" height="35" rx="3"/>
      <rect class="badge" x="811" y="87" width="14" height="23"/>
      <circle class="badge" cx="818" cy="113.5" r="1.5"/>
    </g>

    <g class="connection connection--time">
      <line class="stem" x1="1035" y1="166" x2="1035" y2="203"/>
      <circle class="badge" cx="1035" cy="130" r="36"/>
      <circle class="glyph" cx="1035" cy="130" r="17"/>
      <path class="glyph-line" stroke="var(--badge)" stroke-width="3" d="M1035 119 V131 L1042 137" style="stroke: var(--badge)"/>
    </g>
  </svg>
</main>
</body>
</html>
```